Business Card & Logo Design

Originally the brief was for a card only - I now think it's probably better to include a logo design as well. PLease add $200 to the Budget of $210, Apologies for the inconvenience for thaos that have already submitted designs.

Lamp And Harbor Studios Pty Ltd is a video/dvd/ production company. Primarily corporate medium to high end. It's a one man operation that's been in business 20 years.

The name " Lamp and Harbor" is a primarily a reference to Lucien Marbeck film that's about film making. Shooting "Lamp and harbor" is also a technique employed by cinematographers to make scenes shot in daylight look like night.

See the design emphasising blue day/night tones but open to other ideas.

Main Text can either be Lamp and Harbor Studios or Lamp And Harbor.
Updates

Many thanks to all designers who submitted ideas for this brief.

Choosing between the designs was very difficult indeed.

I wish everyone the best and may the next job be yours!

Walter

Industry/Entity Type

Business

Requirements
Must have
• Text for card:
In Larger Print
Lamp And Harbor Studios or Lamp And Harbor
Walter Brenic
In Smaller Print
Lamp And Harbor Studios Pty Ltd.
17 Calder Lane
Glen Iris, VIC, 3146
P: 9734 2061
m: 0417 385 902
e: walterbrenic@examplemail.net

```html
<!DOCTYPE html>
<html lang="en">
<head>
<meta charset="utf-8">
<title>Lamp and Harbor Studios</title>
<link rel="stylesheet" href="https://fonts.googleapis.com/css2?family=Questrial&family=Open+Sans:wght@400;700&display=swap">
<style>
  :root {
    --sun-deep: #f39a00;
    --sun-mid: #ffd200;
    --sun-light: #fff45a;
    --night: #000000;
    --photo-light: #f4f4f6;
    --photo-mid: #dfe6f0;
    --photo-blue: #b9d4f6;
    --wordmark: #2b2a12;
    --ink: #111111;
  }
  html, body {
    margin: 0;
    padding: 0;
    overflow: hidden;
    background: #ffffff;
  }
  .card {
    position: relative;
    width: 1200px;
    height: 919px;
    overflow: hidden;
  }
  .card__art {
    position: absolute;
    inset: 0;
    display: block;
  }
  .card__text {
    position: absolute;
    left: 20px;
    right: 0;
    margin: 0;
    text-align: center;
  }
  .card__wordmark {
    top: 380px;
    font-family: "Questrial", sans-serif;
    font-weight: 400;
    font-size: 100px;
    letter-spacing: 3px;
    line-height: 1;
    color: var(--wordmark);
  }
  .card__url {
    top: 520px;
    font-family: "Open Sans", sans-serif;
    font-weight: 700;
    font-size: 28px;
    letter-spacing: 0.5px;
    color: var(--ink);
  }
  .card__contact {
    top: 610px;
    font-family: "Open Sans", sans-serif;
    font-weight: 400;
    font-size: 19px;
    line-height: 1.45;
    color: var(--ink);
  }
  .card__person {
    display: block;
    font-family: "Questrial", sans-serif;
    font-size: 34px;
    color: var(--wordmark);
    margin-bottom: 8px;
  }
</style>
</head>
<body>
  <main class="card">
    <svg class="card__art" width="1200" height="919" viewBox="0 0 1200 919">
      <defs>
        <linearGradient id="sun-glow" x1="0" y1="0" x2="1" y2="0">
          <stop offset="0" stop-color="var(--sun-deep)"/>
          <stop offset="0.35" stop-color="var(--sun-mid)"/>
          <stop offset="1" stop-color="var(--sun-light)"/>
        </linearGradient>
        <linearGradient id="photo-tone" x1="0" y1="0" x2="1" y2="0">
          <stop offset="0" stop-color="var(--photo-light)"/>
          <stop offset="0.5" stop-color="var(--photo-mid)"/>
          <stop offset="1" stop-color="var(--photo-blue)"/>
        </linearGradient>
      </defs>

      <rect class="card__day-sky" x="0" y="0" width="593" height="919" fill="url(#sun-glow)"/>
      <rect class="card__night-sky" x="593" y="0" width="607" height="919" fill="var(--night)"/>

      <rect class="card__photo" x="200" y="44" width="840" height="836" fill="url(#photo-tone)"
            role="img" aria-label="Photograph area: silver disc blending into a full blue moon"/>
    </svg>

    <h1 class="card__text card__wordmark">lamp and harbor</h1>
    <p class="card__text card__url">www.lampandharborstudios.com</p>
    <p class="card__text card__contact">
      <span class="card__person">Walter Brenic</span>
      Lamp And Harbor Studios Pty Ltd.<br>
      17 Calder Lane, Glen Iris, VIC, 3146<br>
      P: 9734 2061 &nbsp;&nbsp; m: 0417 385 902<br>
      e: walterbrenic@examplemail.net
    </p>
  </main>
</body>
</html>
```